Lena Corvell Business Card

I need a business card that reflects my current website: itslenacorvell.example and screenshot attached. If we keep the color scheme of the site and sample card below that would be ideal. The business card should include the information on the attached sample cards.

Industry/Entity Type

Business

```html
<!DOCTYPE html>
<html lang="en">
<head>
<meta charset="utf-8">
<title>Lena Corvell Business Card</title>
<link rel="stylesheet" href="https://fonts.googleapis.com/css2?family=Jost:wght@300;400;600&display=swap">
<style>
  :root {
    --backdrop: #e9e8ec;
    --card-white: #ffffff;
    --card-teal: #00b5a7;
    --ink-dark: #111111;
    --ink-light: #ffffff;
    --card-shadow: rgba(40, 40, 60, 0.18);
  }
  * { margin: 0; padding: 0; box-sizing: border-box; }
  html, body {
    width: 1200px;
    height: 934px;
    overflow: hidden;
    background: var(--backdrop);
    font-family: "Jost", sans-serif;
  }
  .canvas {
    position: relative;
    width: 1200px;
    height: 934px;
  }
  .card {
    position: absolute;
    top: 317px;
    width: 525px;
    height: 300px;
    box-shadow: 0 6px 18px var(--card-shadow);
  }
  .card-front {
    left: 60px;
    background: var(--card-white);
  }
  .wordmark {
    position: absolute;
    left: 44px;
    top: 170px;
    font-size: 34px;
    font-weight: 400;
    color: var(--ink-dark);
    letter-spacing: 0.5px;
  }
  .card-back {
    left: 615px;
    background: var(--card-teal);
    color: var(--ink-light);
  }
  .rule {
    position: absolute;
    right: 38px;
    top: 26px;
    width: 1px;
    height: 190px;
    background: var(--ink-light);
  }
  .identity {
    position: absolute;
    right: 52px;
    top: 40px;
    text-align: right;
  }
  .identity-name {
    font-size: 30px;
    font-weight: 300;
    letter-spacing: 1px;
    line-height: 1;
    text-transform: uppercase;
  }
  .identity-roles {
    margin-top: 12px;
    font-size: 12px;
    font-weight: 300;
    letter-spacing: 0.3px;
  }
  .contact {
    position: absolute;
    right: 52px;
    bottom: 34px;
    text-align: right;
    font-size: 12.5px;
    font-weight: 300;
    line-height: 1.55;
  }
  .contact-label { font-weight: 600; }
  .social-mark {
    display: inline-block;
    width: 8px;
    height: 8px;
    margin-right: 5px;
    background: var(--ink-light);
    vertical-align: 0;
  }
</style>
</head>
<body>
<main class="canvas">
  <section class="card card-front" aria-label="Card front">
    <p class="wordmark">Lena Corvell</p>
  </section>

  <section class="card card-back" aria-label="Card back">
    <div class="rule"></div>
    <header class="identity">
      <h1 class="identity-name">Lena Corvell</h1>
      <p class="identity-roles">Brand Curator · Digital Storyteller · Social Entrprenuer</p>
    </header>
    <address class="contact" style="font-style: normal;">
      <p><span class="contact-label">[m]</span> 555.013.2407 · <span class="contact-label">[e]</span> me@lenacorvell.example</p>
      <p><span class="social-mark"></span>@itslenacorvell · <span class="contact-label">[w]</span> www.itslenacorvell.example</p>
    </address>
  </section>
</main>
</body>
</html>
```